Mondaxe custom business card design

Need a authentic, innovative business card design for a new mobile app business. I am uploading a few screen images from our app for you to view. I would like app design theme to match business card design. I can also send logo images.

```html
<!DOCTYPE html>
<html lang="en">
<head>
<meta charset="utf-8">
<title>Mondaxe Business Card</title>
<link rel="stylesheet" href="https://fonts.googleapis.com/css2?family=Montserrat:wght@400;500;600;800&display=swap">
<style>
  :root {
    --stage: #2b2d31;
    --ink: #1c1c1e;
    --paper: #ffffff;
    --violet: #6a2aa6;
    --violet-bright: #8a3fd1;
    --rule: #8c8c90;
  }
  * { box-sizing: border-box; margin: 0; padding: 0; }
  html, body {
    width: 1200px; height: 900px; overflow: hidden;
    background: var(--stage);
    font-family: "Montserrat", sans-serif;
  }
  .card {
    position: absolute; top: 135px;
    width: 360px; height: 630px;
    border-radius: 26px; overflow: hidden;
    box-shadow: 0 18px 40px rgba(0,0,0,.45);
  }
  .card--front { left: 180px; }
  .card--back { left: 660px; }
  .card__art { position: absolute; inset: 0; width: 100%; height: 100%; }

  .brand { position: absolute; left: 0; display: flex; flex-direction: column; align-items: center; }
  .brand__dot { border-radius: 50%; }
  .brand__name { font-weight: 800; letter-spacing: .5px; line-height: 1; }

  .card--front .brand { top: 84px; width: 320px; gap: 12px; }
  .card--front .brand__dot { width: 64px; height: 64px; background: var(--violet); }
  .card--front .brand__name { font-size: 38px; color: var(--ink); }

  .card--back .brand { top: 195px; width: 360px; gap: 22px; }
  .card--back .brand__dot { width: 96px; height: 96px; background: var(--paper); }
  .card--back .brand__name { font-size: 50px; color: var(--paper); }

  .contact {
    position: absolute; left: 0; top: 342px; width: 360px;
    display: flex; flex-direction: column; align-items: center;
    color: var(--paper); text-align: center;
  }
  .contact__name { font-size: 26px; font-weight: 800; letter-spacing: 2px; color: var(--violet-bright); line-height: 1.2; }
  .contact__title { font-size: 16px; font-weight: 500; margin-top: 2px; }
  .contact__rule { width: 250px; height: 1px; background: var(--rule); margin: 13px 0 14px; }
  .contact__icon {
    width: 26px; height: 26px; border-radius: 50%;
    background: var(--violet); display: flex; align-items: center; justify-content: center;
  }
  .contact__icon svg { width: 14px; height: 14px; }
  .contact__line { font-size: 17px; font-weight: 500; margin: 7px 0 11px; }
  .contact__web { font-size: 17px; font-weight: 600; letter-spacing: .5px; }
  .contact__web .accent { color: var(--violet-bright); }
</style>
</head>
<body>

<section class="card card--front" aria-label="Card front">
  <svg class="card__art" viewBox="0 0 360 630" aria-hidden="true">
    <rect width="360" height="630" fill="var(--ink)"/>
    <defs>
      <clipPath id="front-disc"><circle cx="160" cy="140" r="172"/></clipPath>
    </defs>
    <circle cx="160" cy="140" r="172" fill="var(--paper)"/>
    <rect x="-40" y="232" width="420" height="120" fill="var(--violet)" clip-path="url(#front-disc)"/>
    <circle cx="160" cy="-8" r="78" fill="var(--ink)"/>
    <circle cx="160" cy="140" r="183" fill="none" stroke="var(--paper)" stroke-width="6"/>
    <circle cx="311" cy="266" r="17" fill="var(--ink)" stroke="var(--paper)" stroke-width="6"/>
    <path d="M292 252 L300 244 L303 262 Z" fill="var(--ink)"/>
  </svg>

  <div class="brand">
    <span class="brand__dot"></span>
    <span class="brand__name">Mondaxe</span>
  </div>

  <div class="contact">
    <p class="contact__name">YOUR NAME</p>
    <p class="contact__title">Your Title</p>
    <span class="contact__rule"></span>
    <span class="contact__icon">
      <svg viewBox="0 0 24 24"><path fill="#fff" d="M6.6 10.8a15 15 0 0 0 6.6 6.6l2.2-2.2c.3-.3.7-.4 1-.2 1.1.4 2.3.6 3.6.6.6 0 1 .4 1 1V20c0 .6-.4 1-1 1A17 17 0 0 1 3 4c0-.6.4-1 1-1h3.5c.6 0 1 .4 1 1 0 1.3.2 2.5.6 3.6.1.3 0 .7-.2 1z"/></svg>
    </span>
    <p class="contact__line">123-456-2100</p>
    <span class="contact__icon">
      <svg viewBox="0 0 24 24"><path fill="#fff" d="M3 5h18v14H3z"/><path d="M3 5l9 7 9-7" fill="none" stroke="#6a2aa6" stroke-width="2"/></svg>
    </span>
    <p class="contact__line">youremail@mailbox.com</p>
    <span class="contact__rule"></span>
    <p class="contact__web"><span class="accent">www.</span>yourwebsite<span class="accent">.com</span></p>
  </div>
</section>

<section class="card card--back" aria-label="Card back">
  <svg class="card__art" viewBox="0 0 360 630" aria-hidden="true">
    <rect width="360" height="630" fill="var(--paper)"/>
    <circle cx="235" cy="270" r="290" fill="var(--ink)"/>
    <rect x="0" y="300" width="360" height="330" fill="var(--ink)"/>
    <circle cx="340" cy="600" r="250" fill="var(--violet)"/>
    <rect x="0" y="560" width="360" height="70" fill="var(--violet)"/>
  </svg>

  <div class="brand">
    <span class="brand__dot"></span>
    <span class="brand__name">Mondaxe</span>
  </div>
</section>

</body>
</html>
```